New Business Card Design Project

Use the flyer uploaded and website www.brightoakbuilders.com for inspiration.
List Our Services on Backside of business cards
Martin Hollis
Harborline Renovations Inc.
Licensed General Contractors
858-471-9063

Contact Information for Business Card

Use the flyer uploaded and website www.brightoakbuilders.com for inspiration. List Our Services on Backside of business cards Martin Hollis Harborline Renovations Inc. Licensed General Contractors 858-471-9063

```html
<!DOCTYPE html>
<html lang="en">
<head>
<meta charset="utf-8">
<title>Harborline Renovations – Business Card</title>
<link href="https://fonts.googleapis.com/css2?family=Poppins:wght@400;600;700&display=swap" rel="stylesheet">
<style>
  :root {
    --stage: #262626;
    --card: #131313;
    --white: #ffffff;
    --service-text: #c9c9c9;
    --muted: #8a8a8a;
    --detail-text: #d8d8d8;
    --web-text: #6b6b6b;
    --portrait-fill-top: #3a3a3a;
    --portrait-fill-bottom: #1c1c1c;
  }
  * { margin: 0; padding: 0; box-sizing: border-box; }
  html, body {
    width: 1200px; height: 1200px; overflow: hidden;
    background: var(--stage);
    font-family: "Poppins", sans-serif;
  }
  .stage { position: relative; width: 1200px; height: 1200px; }
  .card {
    position: absolute; left: 155px; width: 888px; height: 507px;
    background: var(--card); border-radius: 26px;
  }
  .card--back { top: 79px; }
  .card--front { top: 613px; }

  .brand-name {
    position: absolute; color: var(--white); font-weight: 400;
    letter-spacing: 0.06em; white-space: nowrap; transform: translateX(-50%);
  }
  .card--back .brand-name { left: 262px; top: 292px; font-size: 26px; }
  .card--front .brand-name { left: 790px; top: 80px; font-size: 12px; }

  .services { position: absolute; left: 524px; top: 98px; }
  .services__title { color: var(--white); font-size: 32px; font-weight: 600; line-height: 48px; margin-bottom: 2px; }
  .services__list { list-style: none; }
  .services__list li { color: var(--service-text); font-size: 19px; line-height: 27.4px; }

  .portrait {
    position: absolute; left: 66px; top: 124px; width: 260px; height: 260px;
    border-radius: 50%; border: 9px solid var(--white);
    background: linear-gradient(180deg, var(--portrait-fill-top), var(--portrait-fill-bottom));
  }

  .contact { position: absolute; left: 396px; top: 132px; }
  .contact__name { color: var(--white); font-size: 40px; font-weight: 700; line-height: 44px; }
  .contact__title { color: var(--muted); font-size: 28px; line-height: 38px; margin-bottom: 22px; }
  .contact__line { color: var(--detail-text); font-size: 29px; line-height: 42px; }

  .website {
    position: absolute; left: 0; right: 0; top: 458px; text-align: center;
    color: var(--web-text); font-size: 26px; line-height: 32px;
  }
</style>
</head>
<body>
<main class="stage">
  <section class="card card--back">
    <div class="brand-name">HARBORLINE RENOVATIONS</div>
    <div class="services">
      <h2 class="services__title">Our Services :</h2>
      <ul class="services__list">
        <li>Remodel : Kitchen &amp; Bath</li>
        <li>Painting Interior &amp; Exterior</li>
        <li>Flooring : Carpet, Vinyl, Wood</li>
        <li>Window &amp; Door Replacement</li>
        <li>Plumbing : Repairs &amp; Upgrades</li>
        <li>Energy-Efficient Upgrades</li>
        <li>Deck &amp; Patio Construction</li>
        <li>Water &amp; Mold Damage</li>
        <li>Garage Renovation</li>
      </ul>
    </div>
  </section>

  <section class="card card--front">
    <div class="brand-name">HARBORLINE RENOVATIONS</div>
    <div class="portrait" role="img" aria-label="Profile portrait placeholder"></div>
    <div class="contact">
      <h1 class="contact__name">Martin Hollis</h1>
      <p class="contact__title">CEO Business</p>
      <p class="contact__line">Harborline Renovations Inc.</p>
      <p class="contact__line">Licensed General Contractors</p>
      <p class="contact__line">858-471-9063</p>
    </div>
    <p class="website">www.brightoakbuilders.com</p>
  </section>
</main>
</body>
</html>
```